Financial Planning business needs a new Business Card design

We need a business card design for an Australian financial planning business. I am looking for a clean simple design

Target Market(s)

People aged 25-40

Industry/Entity Type

Financial Service

Contact Information for Business Card

On the front of the card we need the following information:
Name: Colin Merrow (First Name Green: #006838 and last name Grey: #414042)
Position: Financial Adviser
Qualifications: BEc(Hons), AdDipFS(FP), Dip FMBM, CFL®
Mobile: 0437 512 604
Email: colin@brightledgeplan.com.au

On the back of the card we need:
Postal address: PO BOX 5307, PERTH BC, WA 6849
Website: www.brightledgeplan.com.au
Text: AFS Licence No. 518760

The fields need to be able to be edited.

Font styles to use
Sans Serif

Requirements
Must have
• Information listed above

```html
<!DOCTYPE html>
<html lang="en">
<head>
<meta charset="utf-8">
<title>Brightledge Plan – Business Card</title>
<link rel="stylesheet" href="https://fonts.googleapis.com/css2?family=Roboto:wght@400;500&family=Roboto+Condensed:wght@700&family=Source+Sans+3:wght@400&display=swap">
<style>
  :root {
    --green: #006838;
    --grey: #414042;
    --mid-grey: #9a9a9c;
    --white: #ffffff;
    --backdrop: #6e4a2c;
  }
  * { margin: 0; padding: 0; box-sizing: border-box; }
  html, body {
    width: 1200px;
    height: 465px;
    overflow: hidden;
    background: var(--backdrop);
  }
  .canvas {
    position: relative;
    width: 1200px;
    height: 465px;
  }
  .card {
    position: absolute;
    top: 66px;
    width: 540px;
    height: 334px;
    box-shadow: 0 6px 16px rgba(0,0,0,0.35);
  }
  .card--front { left: 40px; background: var(--white); }
  .card--back  { left: 620px; background: var(--green); }

  .wordmark {
    position: absolute;
    font-family: "Roboto Condensed", sans-serif;
    font-weight: 700;
    letter-spacing: 1px;
    line-height: 1;
  }
  .card--front .wordmark {
    left: 28px;
    top: 78px;
    font-size: 52px;
    color: var(--grey);
  }
  .card--back .wordmark {
    left: 0;
    right: 0;
    top: 118px;
    text-align: center;
    font-size: 76px;
    color: var(--white);
  }

  .holder {
    position: absolute;
    right: 22px;
    top: 168px;
    text-align: right;
    font-family: "Roboto", sans-serif;
    color: var(--grey);
  }
  .holder__name { font-size: 25px; font-weight: 400; }
  .holder__first { color: var(--green); }
  .holder__last { color: var(--grey); }
  .holder__role { font-size: 17px; }
  .holder__quals { font-size: 14px; margin-top: 10px; letter-spacing: 0.1px; }

  .divider {
    position: absolute;
    left: 24px;
    right: 0;
    top: 242px;
    height: 2px;
    background: linear-gradient(to right, rgba(154,154,156,0), var(--mid-grey) 60%, var(--mid-grey));
  }

  .contact {
    position: absolute;
    left: 34px;
    top: 264px;
    list-style: none;
    font-family: "Roboto", sans-serif;
    font-size: 16px;
    color: var(--grey);
  }
  .contact li { display: flex; align-items: center; gap: 8px; height: 24px; }
  .contact svg { width: 13px; height: 13px; fill: var(--green); flex: none; }

  .postal {
    position: absolute;
    left: 0;
    right: 0;
    top: 212px;
    list-style: none;
    text-align: center;
    font-family: "Source Sans 3", sans-serif;
    font-size: 16px;
    color: var(--white);
  }
  .postal li { display: flex; justify-content: center; align-items: center; gap: 7px; height: 25px; }
  .postal svg { width: 13px; height: 13px; flex: none; }
</style>
</head>
<body>
<main class="canvas">

  <section class="card card--front" aria-label="Card front">
    <div class="wordmark">BRIGHTLEDGE</div>

    <div class="holder">
      <p class="holder__name"><span class="holder__first">Colin</span> <span class="holder__last">Merrow</span>, <span class="holder__role">Financial Adviser</span></p>
      <p class="holder__quals">BEc(Hons), AdDipFS(FP), Dip FMBM, CFL®</p>
    </div>

    <div class="divider"></div>

    <ul class="contact">
      <li>
        <svg viewBox="0 0 12 12" aria-hidden="true"><path d="M3 0h6a1 1 0 0 1 1 1v10a1 1 0 0 1-1 1H3a1 1 0 0 1-1-1V1a1 1 0 0 1 1-1zm0 1.5v7.5h6V1.5z"/></svg>
        <span>0437 512 604</span>
      </li>
      <li>
        <svg viewBox="0 0 12 12" aria-hidden="true"><path d="M0 5 6 1l6 4v6H0z"/><path d="M1.5 5.5 6 8.3l4.5-2.8" fill="none" stroke="#fff" stroke-width="1"/></svg>
        <span>colin@brightledgeplan.com.au</span>
      </li>
    </ul>
  </section>

  <section class="card card--back" aria-label="Card back">
    <div class="wordmark">BRIGHTLEDGE</div>

    <ul class="postal">
      <li>
        <svg viewBox="0 0 12 12" aria-hidden="true"><path fill="#fff" d="M6 0a4 4 0 0 1 4 4c0 3-4 8-4 8S2 7 2 4a4 4 0 0 1 4-4zm0 2.3A1.7 1.7 0 1 0 6 5.7 1.7 1.7 0 0 0 6 2.3z"/></svg>
        <span>Po Box 5307, Perth BC, WA 6849</span>
      </li>
      <li>
        <svg viewBox="0 0 12 12" aria-hidden="true" fill="none" stroke="#fff" stroke-width="1"><circle cx="6" cy="6" r="5.2"/><ellipse cx="6" cy="6" rx="2.3" ry="5.2"/><path d="M1 6h10M2 3.3h8M2 8.7h8"/></svg>
        <span>www.brightledgeplan.com.au</span>
      </li>
      <li><span>AFS Licence No. 518760</span></li>
    </ul>
  </section>

</main>
</body>
</html>
```